A stationary and business card desgn for a podiatry clinic

i require a stationary design for letter heads, envelopes, buisness cards.

it is for a new podiatry practise within a medical centre, that deals with all lower limb pathology and injury and foot related problems.

the colour scheme for my exisiting logo is orange blue and white. colours provided below.
i would like a white background for the buisness card.

the final design should portray health and wellbeing in a professional manner that still looks modern but sophisticated.

male and female, off all ethinical backgrounds aged between 30-80 years

Medical

• letter head.
need to include all contact details mentioned below.
need to also include ABN 53120978446

i prefer the logo on the top left hand corner and the contact info on the right. the address can be written in a sentence like form as the footer.

Business card
Front:

include logo provided.

clinic details on the front of the card.

Delphine Carrow
B.Pod

P: 7394 5186
F: 7394 5130
M: 0437 612 908
E: delphine@tavrin.com.au
W: www.tavrin.com.au

(may use icons to indicate contact type)

on back

Appointments:

lines to write dates, time etc.
(3-4 of these)
and a small photo of just the foot from the logo in coloured watermark.

Address:
Brackwell Medical Centre
47 Tallowin Street
Brackwell SA 5174
(this location infomation could be in smaller font at the bottom of the buisness card under a line, running in a sentence like fashion) or in the bottom left or right hand corner in a paragraph like you would write it on an envelope

however if you think a different lay out at the back will look better by all means i just need to have room for the appointment even if it is just lines/ space.

i also prefer square cards not rounded corners.

thanks
• plain texts such as times new roman and arial

```html
<!DOCTYPE html>
<html lang="en">
<head>
<meta charset="utf-8">
<title>Tavrin Podiatry Stationery</title>
<link href="https://fonts.googleapis.com/css2?family=Questrial&family=Arimo:wght@400;700&display=swap" rel="stylesheet">
<style>
  :root {
    --orange: #eb5e23;
    --blue: #3b3f97;
    --ink: #222222;
    --grey-text: #555555;
    --paper: #ffffff;
    --backdrop: #e6e6e6;
    --card-font: "Questrial", "Century Gothic", sans-serif;
    --body-font: "Arimo", Arial, sans-serif;
  }
  * { box-sizing: border-box; margin: 0; padding: 0; }
  html, body { width: 1200px; height: 900px; overflow: hidden; }
  body { background: var(--backdrop); position: relative; font-family: var(--card-font); }

  .icon { width: 9px; height: 9px; flex: none; fill: currentColor; }

  /* Letterhead */
  .letterhead { position: absolute; z-index: 1; left: 541px; top: 60px; width: 571px; height: 806px; background: var(--paper); box-shadow: 3px 4px 6px rgba(0,0,0,0.25); }
  .letterhead__band { position: absolute; left: 0; top: 0; width: 571px; height: 21px; background: var(--orange); border-top-right-radius: 16px; }
  .letterhead__contacts { position: absolute; left: 57px; top: 37px; list-style: none; font-family: var(--body-font); font-size: 9.5px; line-height: 11.7px; color: var(--ink); }
  .letterhead__contacts li { display: flex; align-items: center; gap: 4px; }
  .letterhead__contacts .icon { width: 7px; height: 7px; color: #444; }
  .letterhead .brand { position: absolute; left: 362px; top: 50px; font-size: 22px; }
  .letter { position: absolute; left: 56px; top: 170px; width: 474px; font-family: var(--body-font); font-size: 11.2px; line-height: 12.9px; color: var(--ink); }
  .letter p { margin-bottom: 12.9px; }
  .letterhead__rule { position: absolute; left: 0; top: 762px; width: 571px; height: 3px; display: flex; }
  .rule-orange { background: var(--orange); }
  .rule-blue { background: var(--blue); }
  .letterhead__rule .rule-orange { width: 286px; }
  .letterhead__rule .rule-blue { width: 285px; }
  .letterhead__address { position: absolute; left: 61px; top: 771px; font-family: var(--body-font); font-size: 9.3px; letter-spacing: 2.1px; color: var(--orange); }

  /* Business cards */
  .card { position: absolute; z-index: 2; left: 138px; width: 424px; background: var(--paper); overflow: hidden; box-shadow: 3px 4px 6px rgba(0,0,0,0.25); }
  .card--front { top: 268px; height: 237px; }
  .card--back { top: 580px; height: 235px; }
  .card__rule { position: absolute; left: 0; width: 424px; height: 1.5px; display: flex; }
  .card__rule .rule-orange { width: 212px; }
  .card__rule .rule-blue { width: 212px; }
  .card__address { position: absolute; left: 19px; font-size: 12.2px; color: var(--orange); white-space: nowrap; }

  .card__name-tab { position: absolute; left: 0; top: 49px; width: 190px; height: 23px; background: var(--orange); border-top-right-radius: 12px; color: #fff; font-family: var(--body-font); font-weight: 700; font-size: 17px; line-height: 23px; padding-left: 25px; letter-spacing: 0.3px; }
  .card__credential { position: absolute; left: 25px; top: 73px; font-size: 18px; color: var(--orange); }
  .card__contacts { position: absolute; left: 22px; top: 107px; list-style: none; font-size: 13.6px; line-height: 16px; color: var(--ink); }
  .card__contacts li { display: flex; align-items: center; gap: 4px; }
  .card__contacts .icon { color: #333; }
  .card--front .brand { position: absolute; left: 236px; top: 96px; font-size: 22px; }

  .brand { display: flex; align-items: center; gap: 7px; color: var(--blue); font-family: var(--card-font); line-height: 1.05; white-space: nowrap; }
  .brand__dot { width: 0.55em; height: 0.55em; border-radius: 50%; background: var(--orange); flex: none; }

  .card__watermark { position: absolute; left: 0; top: 0; width: 200px; height: 200px; background: radial-gradient(circle at 40% 55%, rgba(246,196,170,0.45) 0%, rgba(246,196,170,0.25) 40%, rgba(190,192,230,0.25) 65%, rgba(255,255,255,0) 80%); }
  .appointments { position: absolute; left: 49px; top: 17px; list-style: none; font-size: 18.5px; color: var(--grey-text); }
  .appointments li { display: flex; height: 35px; align-items: flex-start; }
  .field { display: inline-flex; align-items: flex-end; margin-right: 6px; }
  .field__line { display: inline-block; border-bottom: 1px solid #444; margin-left: 1px; height: 18px; width: 58px; }
</style>
</head>
<body>

<svg width="0" height="0" style="position:absolute" aria-hidden="true">
  <symbol id="i-phone" viewBox="0 0 10 10"><path d="M2 0.5h2l0.6 2.2-1.2 0.9c0.6 1.3 1.6 2.3 2.9 2.9l0.9-1.2 2.2 0.6v2c0 0.6-0.5 1.1-1.1 1.1C4 9 1 6 0.9 1.6 0.9 1 1.4 0.5 2 0.5z"/></symbol>
  <symbol id="i-fax" viewBox="0 0 10 10"><path d="M2.5 0.5h5v2.5h-5z M0.5 3.5h9v4h-2v2h-5v-2h-2z M3.5 7h3v1.8h-3z" fill-rule="evenodd"/></symbol>
  <symbol id="i-mobile" viewBox="0 0 10 10"><path d="M3 0.3h4c0.5 0 0.8 0.3 0.8 0.8v7.8c0 0.5-0.3 0.8-0.8 0.8H3c-0.5 0-0.8-0.3-0.8-0.8V1.1C2.2 0.6 2.5 0.3 3 0.3zM3.2 1.5v5.5h3.6V1.5z" fill-rule="evenodd"/></symbol>
  <symbol id="i-mail" viewBox="0 0 10 10"><path d="M0.5 2h9v6h-9z"/><path d="M0.5 2l4.5 3.5 4.5-3.5" fill="none" stroke="#fff" stroke-width="0.8"/></symbol>
  <symbol id="i-web" viewBox="0 0 10 10"><circle cx="5" cy="5" r="4.5"/><path d="M0.5 5h9M5 0.5v9M2 2.5c2 1 4 1 6 0M2 7.5c2-1 4-1 6 0" fill="none" stroke="#fff" stroke-width="0.6"/></symbol>
</svg>

<!-- Letterhead -->
<section class="letterhead" aria-label="Letterhead">
  <div class="letterhead__band"></div>
  <ul class="letterhead__contacts">
    <li><svg class="icon"><use href="#i-phone"/></svg>7394 5186</li>
    <li><svg class="icon"><use href="#i-fax"/></svg>7394 5130</li>
    <li><svg class="icon"><use href="#i-mobile"/></svg>0437 612 908</li>
    <li><svg class="icon"><use href="#i-mail"/></svg>delphine@tavrin.com.au</li>
    <li><svg class="icon"><use href="#i-web"/></svg>www.tavrin.com.au</li>
  </ul>
  <div class="brand"><span class="brand__dot"></span>Tavrin Podiatry</div>

  <article class="letter">
    <p>Dear Someone Somebody,</p>
    <p>Lorem ipsum dolor sit amet, consectetuer adipiscing elit. Praesent mattis eros a tellus. Quisque leo tortor, commodo id, dapibus et, lacinia et, justo. Ut urna sapien, dictum eu, cursus vel, consectetuer tincidunt, eros. Etiam in libero. Etiam tempor. Maecenas ligula felis, commodo eget, scelerisque id, suscipit nec, odio. Vivamus commodo, magna in mollis feugiat, felis nisl dapibus dolor, eu blandit orci nulla in orci. Cras felis ipsum, mollis at, semper et, tincidunt id, ipsum. Ut consectetuer elit nec elit. Cras luctus molestie ligula. In gravida tempor nunc.</p>
    <p>Curabitur nisl ligula, pulvinar et, volutpat non, porta a, ipsum. Donec tristique ante at est. Pellentesque volutpat est non diam. Aenean vel velit. Suspendisse facilisis nisl et massa. Mauris nec erat. Pellentesque luctus arcu ut dui. Proin suscipit lorem id augue. Maecenas eget ipsum nec orci convallis viverra. Suspendisse potenti. Donec sed enim. Ut et turpis. Ut mattis enim nec nisl. Ut quam. Pellentesque lobortis vehicula risus.</p>
    <p>Etiam massa erat, tempor et, elementum fringilla, pellentesque ac, odio. Cras sed felis. Aliquam erat volutpat. Etiam tristique. Donec pellentesque, nulla semper adipiscing faucibus, nibh augue semper sapien, eget feugiat dui massa et urna. Nullam ac arcu. Quisque interdum. Morbi tristique sagittis arcu. Phasellus euismod ante eget risus. Nam convallis rutrum augue. Pellentesque placerat ultrices tellus.</p>
    <p>Ut lacinia. Sed aliquet diam at odio. Nunc ultrices pretium urna. Sed risus velit, nonummy eget, suscipit at, sagittis in, tortor. Quisque risus. Duis porta. Nunc blandit, augue et nonummy ultrices, lacus justo tincidunt nibh, eu vestibulum turpis metus iaculis ipsum. Morbi neque. Quisque augue. Etiam eleifend rhoncus metus. Aliquam auctor libero non nisi.</p>
    <p>Pellentesque habitant morbi tristique senectus et netus et malesuada fames ac turpis egestas. Nullam justo lectus, lobortis id, pharetra eu, pulvinar ac, nibh. Sed hendrerit pretium urna. Vivamus ut ipsum eget justo adipiscing adipiscing. Donec lectus arcu, interdum eget, malesuada a, euismod sed, sapien. Proin imperdiet, nulla sit amet mattis adipiscing, enim nibh condimentum metus, sit amet lacinia tortor arcu eget magna. Mauris eget enim at ante luctus ultricies. Integer eu nunc eget tellus iaculis vestibulum. Suspendisse potenti. Aenean aliquam mauris id turpis.</p>
    <p>Your Sincerely,<br>Owen Lessard.</p>
  </article>

  <div class="letterhead__rule"><span class="rule-orange"></span><span class="rule-blue"></span></div>
  <p class="letterhead__address">Brackwell Medical Centre • 47 Tallowin Street • Brackwell SA 5174</p>
</section>

<!-- Business card, front -->
<section class="card card--front" aria-label="Business card front">
  <div class="card__name-tab">Delphine Carrow</div>
  <div class="card__credential">B.Pod</div>
  <ul class="card__contacts">
    <li><svg class="icon"><use href="#i-phone"/></svg>7394 5186</li>
    <li><svg class="icon"><use href="#i-fax"/></svg>7394 5130</li>
    <li><svg class="icon"><use href="#i-mobile"/></svg>0437 612 908</li>
    <li><svg class="icon"><use href="#i-mail"/></svg>delphine@tavrin.com.au</li>
    <li><svg class="icon"><use href="#i-web"/></svg>www.tavrin.com.au</li>
  </ul>
  <div class="brand"><span class="brand__dot"></span>Tavrin Podiatry</div>
  <div class="card__rule" style="top:203px"><span class="rule-orange"></span><span class="rule-blue"></span></div>
  <p class="card__address" style="top:207px">Brackwell Medical Centre ● 47 Tallowin Street ● Brackwell SA 5174</p>
</section>

<!-- Business card, back -->
<section class="card card--back" aria-label="Business card back">
  <div class="card__watermark" role="img" aria-label="Faint coloured foot watermark"></div>
  <ul class="appointments">
    <li><span class="field">Date:<span class="field__line"></span></span><span class="field">Day:<span class="field__line"></span></span><span class="field">Time:<span class="field__line"></span></span></li>
    <li><span class="field">Date:<span class="field__line"></span></span><span class="field">Day:<span class="field__line"></span></span><span class="field">Time:<span class="field__line"></span></span></li>
    <li><span class="field">Date:<span class="field__line"></span></span><span class="field">Day:<span class="field__line"></span></span><span class="field">Time:<span class="field__line"></span></span></li>
    <li><span class="field">Date:<span class="field__line"></span></span><span class="field">Day:<span class="field__line"></span></span><span class="field">Time:<span class="field__line"></span></span></li>
    <li><span class="field">Date:<span class="field__line"></span></span><span class="field">Day:<span class="field__line"></span></span><span class="field">Time:<span class="field__line"></span></span></li>
  </ul>
  <div class="card__rule" style="top:200px"><span class="rule-orange"></span><span class="rule-blue"></span></div>
  <p class="card__address" style="top:204px">Brackwell Medical Centre ● 47 Tallowin Street ● Brackwell SA 5174</p>
</section>

</body>
</html>
```